Dr. Pelham Billboard Sign Design

Family Dental Practice looking for a billboard sign design. We have Attached a Image of Dr Pelham and Her horse she would like to incorporate. The size of the sign is 118" tall and 196" Wide. We hired a previous designer to work on this also but would like to see what other come up with before we decide on a final. Please use something similar for a animal shelter icon to go beside the Animal Shelter Discount statement. You can use the text from the postcard file attached. I know text adjustments will be needed, but more interested in a eye catching design. Themes: Fall/Winter/Mountains/Nature , colors: open but Dr P like purple. We are open to ideas and will answer any questions.
TEXT
Theme: Fall/Winter/Mountain
Image: Dr Pelham with Horse (Same from mailer design)
Text to Keep that needs to be bold and Priority
1. Dr. Rosalind Pelham Family Dentistry
314 Brellin Court Cedarholm, TN 28094
555-413-5276 | RPelhamDDS@Velmorx.net
(FaceBook icon) RosalindPelhamDDS
2. ACCEPTING NEW PATIENTS
3. Affordable Dentistry for Your Whole Family
4. WE FILE YOUR INSURANCE CLAIMS
5. Discounts for Senior Citizens, Law Enforcement, First Responders, Military Personnel, State Employees and College Students
6. (Cool Animal Shelter Icon) WE OFFER A DISCOUNT TO PATIENTS WHO SUPPORT OUR LOCAL ANIMAL SHELTERS BY ADOPTING, DONATING OR VOLUNTEERING
7. Schedule Your Appointment TODAY!
Target Market(s)
Local Community to Bring in Patients to dental office
Industry/Entity Type
Dental
Look and feel

```html
<!DOCTYPE html>
<html lang="en">
<head>
<meta charset="utf-8">
<title>Dr. Pelham Family Dentistry Billboard</title>
<link rel="stylesheet" href="https://fonts.googleapis.com/css2?family=Montserrat:wght@700;800;900&family=Nunito:wght@800;900&display=swap">
<style>
  :root {
    --purple: #652d91;
    --yellow: #fff200;
    --red: #ed1c24;
    --white: #ffffff;
    --social: #3b5998;
    --autumn-dark: #3d3218;
    --autumn-mid: #7a6328;
    --autumn-warm: #b8772e;
    --autumn-leaf: #c9562a;
  }
  html, body { margin: 0; padding: 0; overflow: hidden; background: #fff; }
  .billboard {
    position: relative; width: 1200px; height: 722px; overflow: hidden;
    font-family: "Montserrat", sans-serif;
  }
  .scene-photo {
    position: absolute; inset: 0;
    background:
      radial-gradient(ellipse at 60% 30%, rgba(200,170,80,.55), transparent 55%),
      linear-gradient(180deg, var(--autumn-mid) 0%, var(--autumn-dark) 45%, var(--autumn-warm) 75%, var(--autumn-leaf) 100%);
  }
  .portrait-photo {
    position: absolute; left: 262px; top: 196px; width: 460px; height: 526px;
    background: radial-gradient(ellipse at 50% 55%, #8a4a2e 0%, #5a3322 45%, rgba(90,51,34,0) 75%);
  }
  .shapes { position: absolute; inset: 0; }
  .headline { position: absolute; left: 0; top: 0; }
  .insurance-badge {
    position: absolute; left: 20px; top: 36px; width: 202px;
    text-align: center; color: var(--purple);
    font: 800 27px/25px "Montserrat", sans-serif; text-transform: uppercase;
  }
  .schedule-burst {
    position: absolute; left: 42px; top: 400px; width: 200px; text-align: center;
    transform: rotate(-20deg); color: var(--yellow);
    font-family: "Montserrat", sans-serif; font-weight: 800;
  }
  .schedule-burst .lead { font-size: 23px; line-height: 23px; display: block; }
  .schedule-burst .today { font-size: 42px; line-height: 44px; font-weight: 900; display: block; }
  .new-patients {
    position: absolute; left: 16px; top: 652px; color: var(--yellow); text-align: center;
    width: 232px; font-family: "Montserrat", sans-serif; font-weight: 900; text-transform: uppercase;
  }
  .new-patients .big { display: block; font-size: 35px; line-height: 36px; letter-spacing: -.5px; }
  .new-patients .small { display: block; font-size: 25px; line-height: 24px; font-weight: 800; }
  .discounts-band {
    position: absolute; left: 684px; top: 258px; width: 516px; height: 92px;
    background: var(--purple); color: var(--white); text-align: center; box-sizing: border-box; padding: 4px 10px 0 40px;
  }
  .discounts-band h2 { margin: 0; font: 900 26px/30px "Nunito", sans-serif; }
  .discounts-band p {
    margin: 0; font: 700 14.4px/19.5px "Montserrat", sans-serif; text-transform: uppercase; letter-spacing: .6px; word-spacing: 2px;
  }
  .shelter-band {
    position: absolute; left: 674px; top: 366px; width: 526px; height: 80px;
    background: var(--yellow); color: var(--purple);
  }
  .shelter-icon { position: absolute; left: 16px; top: 8px; width: 64px; height: 64px; }
  .shelter-text {
    position: absolute; left: 92px; top: 5px; width: 392px; margin: 0; text-align: center;
    font: 800 14.6px/19.5px "Montserrat", sans-serif; text-transform: uppercase; letter-spacing: .4px;
  }
  .shelter-text .word-strong { font-size: 26px; font-weight: 900; letter-spacing: 0; vertical-align: -2px; }
  .practice-contact {
    position: absolute; right: 12px; top: 574px; text-align: right; color: var(--white);
    font-family: "Nunito", sans-serif; font-style: normal;
  }
  .practice-contact .name { color: var(--yellow); font: 900 22px/26px "Nunito", sans-serif; }
  .practice-contact .detail { font: 800 13px/18px "Montserrat", sans-serif; }
  .practice-contact .phone { color: var(--yellow); font: 900 26px/32px "Nunito", sans-serif; }
  .practice-contact .email, .practice-contact .social { color: var(--yellow); font: 800 16px/23px "Nunito", sans-serif; }
  .social-mark {
    display: inline-block; width: 15px; height: 15px; background: var(--social); margin-right: 6px; vertical-align: -2px;
  }
</style>
</head>
<body>
<main class="billboard">
  <div class="scene-photo" role="img" aria-label="Autumn tree-lined country lane with a wooden fence and fallen leaves"></div>
  <div class="portrait-photo" role="img" aria-label="Dr. Pelham standing cheek to cheek with her brown horse"></div>

  <svg class="shapes" width="1200" height="722" viewBox="0 0 1200 722" aria-hidden="true">
    <path d="M0 0 H1200 V120 C1120 150 1050 180 960 180 C700 182 420 130 224 130 V0 Z" fill="var(--yellow)"/>
    <path d="M0 0 H1200 V112 C1120 142 1050 170 960 170 C700 172 420 124 224 124 V0 Z" fill="var(--purple)"/>
    <path d="M0 0 H20 V152 L0 152 Z" fill="var(--purple)"/>
    <path d="M14 0 H228 V160 L121 248 L14 160 Z" fill="var(--purple)"/>
    <path d="M20 0 H222 V156 L121 240 L20 156 Z" fill="var(--yellow)"/>
    <polygon fill="var(--red)" points="
      140,352 152,372 166,356 174,378 190,364 194,388 212,378 212,402 232,396 226,418 248,418 238,438 260,444 244,458 264,472 244,484 260,500 238,506 248,526 226,526 232,548 212,542 212,566 194,556 190,580 174,566 166,588 152,572 140,592 128,572 114,588 106,566 90,580 86,556 68,566 68,542 48,548 54,526 32,526 42,506 20,500 36,484 16,472 36,458 20,444 42,438 32,418 54,418 48,396 68,402 68,378 86,388 90,364 106,378 114,356 128,372"/>
    <path d="M792 722 C880 600 1000 514 1200 510 V722 Z" fill="var(--yellow)"/>
    <path d="M804 722 C890 610 1010 526 1200 522 V722 Z" fill="var(--purple)"/>
  </svg>

  <svg class="headline" width="1200" height="130" viewBox="0 0 1200 130" role="heading" aria-level="1" aria-label="Affordable Dentistry for Your Whole Family">
    <text x="244" y="64" textLength="872" lengthAdjust="spacingAndGlyphs" fill="var(--yellow)" font-family="Montserrat, sans-serif" font-weight="800" font-size="66">AFFORDABLE DENTISTRY</text>
    <text x="244" y="120" textLength="906" lengthAdjust="spacingAndGlyphs" fill="var(--yellow)" font-family="Montserrat, sans-serif" font-weight="800" font-size="66">FOR YOUR WHOLE FAMILY</text>
  </svg>

  <div class="insurance-badge">We File<br>Your<br>Insurance<br>Claims</div>

  <div class="schedule-burst">
    <span class="lead">Schedule<br>Your<br>Appointment</span>
    <span class="today">TODAY!</span>
  </div>

  <div class="new-patients">
    <span class="big">Accepting</span>
    <span class="small">New Patients</span>
  </div>

  <section class="discounts-band">
    <h2>Discounts</h2>
    <p>For senior citizens, law enforcement,<br>first responders, military personnel,<br>state employees and college students</p>
  </section>

  <section class="shelter-band">
    <svg class="shelter-icon" viewBox="0 0 64 64" aria-hidden="true">
      <circle cx="32" cy="32" r="28" fill="var(--white)" stroke="var(--purple)" stroke-width="4"/>
    </svg>
    <p class="shelter-text">We offer a <span class="word-strong">Discount</span> to patients<br>who support our local animal shelters<br>by adopting, donating or volunteering</p>
  </section>

  <address class="practice-contact">
    <div class="name">Dr. Rosalind Pelham</div>
    <div class="detail">Family Dentistry</div>
    <div class="detail">314 Brellin Court Cedarholm, TN 28094</div>
    <div class="phone">555-413-5276</div>
    <div class="email">RPelhamDDS@Velmorx.net</div>
    <div class="social"><span class="social-mark"></span>RosalindPelhamDDS</div>
  </address>
</main>
</body>
</html>
```